Multi-Faceted Legal and Finanacial Advisory Group Needs Business Card Design

We need a business card design for a newly branded Orlando Florida area advising group consisting of Attorneys, Accountants and Financial Planners. The company is named RT Counsel Group. You will find our initial work on a business card. The information on the business card are merely guideposts and not final product. The logo does not have the be the same as provided since we have not finalized the logo. We would like to stay with a black/white/grey color scheme, but limited use of color is not out of the question.

Target Market(s)

Businesses and their Corporate Representatives

Industry/Entity Type

Business

Contact Information for Business Card

Should have Name, Title, Phone, Cell, Fax, Email and website. Logo should incorporate RT in some fashion however final logo used does not have to be the one on the document provided.

Requirements
Must have
• An RT design on front and back.

```html
<!DOCTYPE html>
<html lang="en">
<head>
<meta charset="utf-8">
<title>RT Counsel Group – Business Card</title>
<link href="https://fonts.googleapis.com/css2?family=Montserrat:wght@400;500;600&display=swap" rel="stylesheet">
<style>
  :root {
    --page: #e6e6e6;
    --card-white: #fafafa;
    --card-grey: #9a9a9a;
    --card-black: #0b0b0b;
    --ink: #3a3a3a;
    --accent: #5a7fa6;
    --text-light: #f2f2f2;
    --text-muted: #c8c8c8;
  }
  * { box-sizing: border-box; margin: 0; padding: 0; }
  html, body { width: 1200px; height: 828px; overflow: hidden; }
  body {
    background: var(--page);
    font-family: "Montserrat", sans-serif;
    display: flex;
    align-items: center;
    justify-content: center;
    gap: 56px;
  }
  .card {
    position: relative;
    width: 520px;
    height: 297px;
    background: linear-gradient(135deg, #ffffff 0%, var(--card-white) 60%, #ececec 100%);
    box-shadow: 0 10px 24px rgba(0,0,0,0.18);
    overflow: hidden;
  }
  .brand {
    position: absolute;
    display: flex;
    align-items: center;
    gap: 10px;
    color: var(--ink);
    font-weight: 500;
    letter-spacing: 0.02em;
    border: 2px solid var(--accent);
    background: #ffffff;
    white-space: nowrap;
  }
  .brand-square { width: 20px; height: 20px; background: var(--accent); }
  .card-front .brand {
    left: 50%; top: 50%;
    transform: translate(-50%, -50%);
    font-size: 20px;
    padding: 14px 20px;
  }
  .card-back .brand { left: 60px; top: 58px; font-size: 16px; padding: 10px 14px; gap: 8px; }
  .card-back .brand-square { width: 16px; height: 16px; }
  .back-shapes { position: absolute; inset: 0; }
  .person {
    position: absolute; left: 34px; bottom: 38px;
    color: var(--text-light);
  }
  .person-name { font-size: 13px; font-weight: 500; letter-spacing: 0.06em; text-transform: uppercase; }
  .person-title { font-size: 9px; letter-spacing: 0.08em; text-transform: uppercase; color: var(--text-muted); margin-top: 3px; }
  .address {
    position: absolute; left: 262px; top: 150px;
    color: var(--text-light); font-size: 9.5px; line-height: 1.5; letter-spacing: 0.03em;
  }
  .contact {
    position: absolute; top: 202px;
    list-style: none;
    color: var(--text-light); font-size: 8.5px; letter-spacing: 0.03em;
  }
  .contact-phones { left: 262px; }
  .contact-web { left: 372px; }
  .contact li { display: flex; align-items: center; gap: 6px; height: 16px; white-space: nowrap; }
  .contact svg { width: 9px; height: 9px; fill: none; stroke: var(--text-light); stroke-width: 1.3; flex: none; }
</style>
</head>
<body>
  <section class="card card-front" aria-label="Card front">
    <div class="brand"><span class="brand-square"></span>RT Counsel Group</div>
  </section>

  <section class="card card-back" aria-label="Card back">
    <svg class="back-shapes" viewBox="0 0 520 297" preserveAspectRatio="none" aria-hidden="true">
      <path d="M0,160 C180,155 380,95 520,0 L520,297 L0,297 Z" fill="var(--card-grey)"/>
      <path d="M0,175 C180,170 380,110 520,15 L520,297 L0,297 Z" fill="var(--card-black)"/>
    </svg>
    <div class="brand"><span class="brand-square"></span>RT Counsel Group</div>

    <div class="address">214 Pine Lake Avenue<br>Winter Park FL</div>

    <ul class="contact contact-phones">
      <li><svg viewBox="0 0 10 10"><path d="M2,1 L4,1 L5,3 L4,4 Q5,6 6,6 L7,5 L9,6 L9,8 Q5,9 2,5 Q1,3 2,1 Z"/></svg>407 555 0142</li>
      <li><svg viewBox="0 0 10 10"><rect x="1" y="4" width="8" height="4"/><path d="M3,4 L3,1 L7,1 L7,4 M3,8 L3,9 L7,9 L7,8"/></svg>Fax 407 555 0199</li>
    </ul>
    <ul class="contact contact-web">
      <li><svg viewBox="0 0 10 10"><rect x="1" y="2" width="8" height="6"/><path d="M1,2 L5,5.5 L9,2"/></svg>info@rtcounsel.com</li>
      <li><svg viewBox="0 0 10 10"><circle cx="5" cy="5" r="4"/><path d="M1,5 L9,5 M5,1 Q2.5,5 5,9 M5,1 Q7.5,5 5,9"/></svg>www.rtcounsel.com</li>
    </ul>

    <div class="person">
      <div class="person-name">Dana Whitfield</div>
      <div class="person-title">President</div>
    </div>
  </section>
</body>
</html>
```